Modern Lawfirm Business Card Design

We're looking for a business card to incorporate the newly created logo we had made.

Ideally looking for a law firm business card demonstrating, modern, minimalist, strong/bold design.

I'm open to any design honestly, but nothing "flashy".

Target Market(s)

Immigration law, family immigration, humanitarian, general legal

Industry/Entity Type

Law Firm

Contact Information for Business Card

Please use dummy information, name, street address, city, state, phone number, email, website.

Font styles to use
Serif
Sans Serif

Requirements
Must have
• Please use dummy information, name, street address, city, state, phone number, email, website.

```html
<!DOCTYPE html>
<html lang="en">
<head>
<meta charset="utf-8">
<title>Valera Immigration Law – Business Cards</title>
<link href="https://fonts.googleapis.com/css2?family=Cinzel:wght@600&family=Open+Sans:wght@400;600&display=swap" rel="stylesheet">
<style>
  :root {
    --bg: #ece9e4;
    --blue: #1f5fa6;
    --blue-bright: #2766b8;
    --blue-deep: #17518f;
    --grey: #55575c;
    --paper: #f7f7f7;
    --paper-shade: #e4e4e4;
    --white: #ffffff;
  }
  * { margin: 0; padding: 0; box-sizing: border-box; }
  html, body { width: 1200px; height: 1023px; overflow: hidden; background: var(--bg); }
  body { position: relative; font-family: "Open Sans", Arial, sans-serif; }

  .card {
    position: absolute;
    width: 620px;
    height: 354px;
    border-radius: 4px;
    overflow: hidden;
    box-shadow: 0 10px 24px rgba(0,0,0,.18);
  }

  /* Front */
  .card--front {
    left: 60px; top: 80px;
    background: linear-gradient(135deg, var(--white), var(--paper) 55%, var(--paper-shade));
  }
  .front__brand {
    position: absolute; left: 56px; top: 96px;
    display: flex; align-items: center; gap: 14px;
  }
  .brand-square { width: 22px; height: 22px; background: var(--blue); }
  .brand-name {
    font-family: "Cinzel", Georgia, serif; font-weight: 600;
    color: var(--blue); line-height: 1.1;
  }
  .front__brand .brand-name { font-size: 40px; }
  .brand-name .sub { display: block; font-size: .32em; letter-spacing: .6em; margin-top: 6px; }

  .front__contact {
    position: absolute; left: 360px; top: 60px; width: 260px; height: 170px;
    background: var(--grey); color: var(--white);
    padding: 26px 24px; font-size: 13px; line-height: 1.6;
  }
  .contact-row { display: flex; align-items: center; gap: 9px; }
  .contact-row svg { width: 12px; height: 12px; flex: none; }
  .contact-address { margin-top: 14px; padding-left: 21px; line-height: 1.45; }

  .front__nameband {
    position: absolute; left: 215px; top: 216px; width: 210px; height: 72px;
    background: var(--blue-bright); color: var(--white);
    padding: 16px 20px;
    border: 3px solid var(--white); border-left: none;
  }
  .front__strip {
    position: absolute; left: 150px; top: 230px; width: 70px; height: 58px;
    background: var(--blue-bright);
  }
  .person-name { font-size: 19px; font-weight: 600; line-height: 1.1; }
  .person-role { font-size: 13px; margin-top: 3px; }

  /* Back */
  .card--back {
    left: 520px; top: 580px;
    background: linear-gradient(135deg, var(--blue-bright), var(--blue-deep));
  }
  .back__brand {
    position: absolute; left: 180px; top: 120px;
    display: flex; align-items: center; gap: 18px;
  }
  .back__brand .brand-square { background: var(--white); width: 26px; height: 26px; }
  .back__brand .brand-name { color: var(--white); font-size: 52px; }
  .back__web {
    position: absolute; left: 40px; top: 177px;
    transform: translateY(-50%) rotate(-90deg); transform-origin: left center;
    color: var(--white); font-size: 12px; letter-spacing: .32em;
    margin-top: 110px;
  }
</style>
</head>
<body>
  <section class="card card--front" aria-label="Business card front">
    <div class="front__brand">
      <span class="brand-square"></span>
      <span class="brand-name">Valera<span class="sub">Immigration Law</span></span>
    </div>

    <div class="front__contact">
      <div class="contact-row">
        <svg viewBox="0 0 12 12"><path d="M3 1l2 2-1 1.5c.6 1.4 1.6 2.4 3 3L8.5 6.5l2 2-1.5 1.5C5 9.5 2.5 7 2 3z" fill="currentColor"/></svg>
        +555 014 2280
      </div>
      <div class="contact-row">
        <svg viewBox="0 0 12 12"><rect x="1" y="2.5" width="10" height="7" fill="none" stroke="currentColor"/><path d="M1 2.5l5 4 5-4" fill="none" stroke="currentColor"/></svg>
        info@valeralaw.com
      </div>
      <div class="contact-row">
        <svg viewBox="0 0 12 12"><circle cx="6" cy="6" r="5" fill="none" stroke="currentColor"/><path d="M1 6h10M6 1c-2.5 3-2.5 7 0 10M6 1c2.5 3 2.5 7 0 10" fill="none" stroke="currentColor"/></svg>
        www.valeralaw.com
      </div>
      <p class="contact-address">here your company or<br>home address</p>
    </div>

    <div class="front__strip"></div>
    <div class="front__nameband">
      <p class="person-name">Daniel Reyes</p>
      <p class="person-role">Founder</p>
    </div>
  </section>

  <section class="card card--back" aria-label="Business card back">
    <div class="back__brand">
      <span class="brand-square"></span>
      <span class="brand-name">Valera<span class="sub">Immigration Law</span></span>
    </div>
    <p class="back__web">www.valeralaw.com</p>
  </section>
</body>
</html>
```